https://www.lernwinkel.de - a website for school website in germany for presentation/paper download

we own the webpage https://www.lernwinkel.de and we need a new webdesign (a new website logo is also possible). we want only new images and css, we don´t want to made any change to the HTML code.
we need only new images/color for a new modern look.

we want to have more trust to our user. they have to download presentation/paper
we need template for this sites:
https://www.lernwinkel.de/
https://www.lernwinkel.de/referate/englisch
https://www.lernwinkel.de/forum.php
https://www.lernwinkel.de/forum/insektenhotel/258614
https://www.lernwinkel.de/referat/latein/sokrates/25892
https://www.lernwinkel.de/schule_seminararbeit_fachliste.php?fach=238
and other sites on the website. (take a look around the website)

we don´t like white color for sublines or text. (h1/h2/strong) . in image are white Text OK.

important: we want to chance ONLY the CSS and PICS, we don´t want to remove or chance any HTML code.

after you have made a mockup of the new design and we give you a go, you have to made a package with the IMAGES and the CSS rules (text how we have to chance the current css)

Target Market(s)

Germany, Austria, Switzerland -DACH

Industry/Entity Type

School

Coding

Coded - Design and coding required

Number of Pages Required

5+ page

Font styles to use
Serif
Sans Serif

Colors

Designer to choose colors to be used in the design.

Requirements
Must have
• We want only to remove images and no HTML Code
Should not have
• NO white colors for Text on the site. In images are OK

```html
<!DOCTYPE html>
<html lang="en">
<head>
<meta charset="utf-8">
<title>Lernwinkel.de</title>
<link href="https://fonts.googleapis.com/css2?family=Open+Sans:ital,wght@0,400;0,600;0,700;1,400&display=swap" rel="stylesheet">
<style>
:root{
  --dark:#211f05;
  --olive:#8f9a12;
  --orange:#e09b12;
  --ink:#2a2805;
  --text:#555;
  --line:#b5b5b5;
  --white:#fff;
}
*{box-sizing:border-box;margin:0;padding:0}
html,body{width:1200px;height:1195px;overflow:hidden;background:#fff;font-family:"Open Sans",sans-serif;color:var(--text)}
.stage{position:absolute;left:0;top:0;width:1400px;height:1394px;transform:scale(.857143);transform-origin:0 0}
.abs{position:absolute}
.shelf-left{left:0;top:455px;width:115px;height:495px;background:linear-gradient(90deg,#c9a7ad 0,#9b7f86 35%,#b59a80 60%,#8b6e5e 100%)}
.shelf-right{left:1285px;top:480px;width:115px;height:470px;background:linear-gradient(90deg,#8da98a 0,#3c5a4a 40%,#5c8a8a 70%,#3f6c7a 100%)}
.page{left:115px;top:0;width:1170px;height:1394px;background:var(--white);box-shadow:0 0 14px rgba(0,0,0,.12)}
.topbar{left:115px;top:0;width:1170px;height:101px;background:var(--dark)}
.brand{left:135px;top:22px;color:var(--white)}
.brand-name{font-size:40px;font-weight:400;line-height:1;display:flex;align-items:center;gap:12px}
.brand-name i{display:inline-block;width:16px;height:16px;background:var(--white)}
.brand-tag{font-size:10px;margin-top:8px;margin-left:28px}
.mainnav{left:607px;top:40px;display:flex;gap:38px;color:var(--white);font-weight:700;font-size:18px;text-transform:uppercase}
.mainnav span{display:flex;align-items:center;gap:8px}
.login-pill{left:1135px;top:26px;width:126px;height:50px;border:2px solid var(--white);border-radius:25px;color:var(--white);font-weight:700;font-size:18px;display:flex;align-items:center;justify-content:center;gap:8px}
.subnav{left:115px;top:101px;width:1170px;height:48px;border-bottom:1px solid #ccc;display:flex;gap:45px;padding-left:18px;align-items:center;font-size:17px;color:#333}
.box{border:1px solid var(--line);background:#fff}
.box-head{height:47px;border-bottom:1px solid var(--line);display:flex;align-items:center;gap:9px;padding-left:16px;font-weight:700;font-size:18px;color:var(--ink)}
.list{list-style:none;padding:18px 0 0 17px}
.list li{height:39px;display:flex;align-items:center;gap:8px;font-size:16px;color:var(--text)}
.tick{width:13px;height:13px;border-radius:50%;background:var(--olive);position:relative;flex:none}
.tick::after{content:"";position:absolute;left:4px;top:2px;width:3px;height:6px;border:solid #fff;border-width:0 2px 2px 0;transform:rotate(45deg)}
.stats{padding:14px 14px 0 17px}
.stats div{height:39px;display:flex;justify-content:space-between;align-items:center;font-size:16px}
.search{left:374px;top:213px;width:652px;height:76px;background:var(--olive)}
.search label{position:absolute;left:16px;top:29px;color:var(--white);font-size:16px;font-weight:600}
.search .field{position:absolute;left:111px;top:14px;width:387px;height:48px;background:#fff}
.btn{display:flex;align-items:center;justify-content:center;border-radius:24px;font-weight:700;font-size:16px;text-transform:uppercase}
.btn-orange{background:var(--orange);color:var(--white)}
.btn-ghost{border:1px solid #999;color:var(--orange);background:#fff}
.hero{left:374px;top:311px;width:652px;height:295px;background:linear-gradient(100deg,#3b3430 0,#5e5148 45%,#7a6a5a 70%,#2e2a28 100%)}
.hero-text{left:403px;top:340px;width:400px;color:var(--white)}
.hero-text h1{font-size:25px;font-weight:700;margin-bottom:14px}
.hero-text p{font-size:14.5px;line-height:33px}
.hero-text b{font-size:17px}
.subjects{left:374px;top:627px;width:652px;height:396px}
.grid{position:absolute;top:90px;left:20px;font-size:14px}
.col{position:absolute;top:0}
.col span{height:39px;display:flex;align-items:center;gap:8px;white-space:nowrap;position:absolute}
.messenger{left:1044px;top:213px;width:223px;height:273px}
.promo{left:1044px;top:504px;width:223px;height:273px;background:linear-gradient(160deg,#a4553e 0,#6b4a3a 40%,#2c2e45 75%,#4a3c36 100%)}
.footer{left:115px;top:1291px;width:1170px;height:103px;background:var(--dark);color:var(--white);text-align:center;font-size:15px}
</style>
</head>
<body>
<div class="stage">
  <div class="abs shelf-left" role="img" aria-label="Row of standing books along the left edge"></div>
  <div class="abs shelf-right" role="img" aria-label="Row of standing books along the right edge"></div>
  <div class="abs page"></div>

  <header>
    <div class="abs topbar"></div>
    <div class="abs brand">
      <div class="brand-name"><i></i>Lernwinkel.de</div>
      <div class="brand-tag">Referate, Hausaufgaben und nette Leute kennen lernen</div>
    </div>
    <nav class="abs mainnav">
      <span><svg width="18" height="16" viewBox="0 0 18 16"><path d="M9 1 1 8h2v7h5v-5h2v5h5V8h2z" fill="#fff"/></svg>Start</span>
      <span><svg width="22" height="18" viewBox="0 0 22 18"><circle cx="11" cy="5" r="4" fill="#fff"/><circle cx="4" cy="6" r="3" fill="#fff"/><circle cx="18" cy="6" r="3" fill="#fff"/><path d="M4 17c0-5 3-7 7-7s7 2 7 7z M0 15c0-4 2-5 4-5v5z M22 15c0-4-2-5-4-5v5z" fill="#fff"/></svg>Community</span>
      <span><svg width="22" height="16" viewBox="0 0 22 16"><path d="M1 0v15h21" stroke="#fff" stroke-width="2" fill="none"/><rect x="5" y="7" width="2.5" height="6" fill="#fff"/><rect x="9" y="3" width="2.5" height="10" fill="#fff"/><rect x="13" y="5" width="2.5" height="8" fill="#fff"/><rect x="17" y="9" width="2.5" height="4" fill="#fff"/></svg>Presentations</span>
    </nav>
    <div class="abs login-pill"><svg width="14" height="17" viewBox="0 0 14 17"><path d="M3 8V5a4 4 0 0 1 8 0v3" stroke="#fff" stroke-width="2" fill="none"/><rect x="1" y="8" width="12" height="9" rx="1" fill="#fff"/></svg>LOGIN</div>
    <nav class="abs subnav"><span>Forums</span><span>Members</span><span>Flirt search</span></nav>
  </header>

  <aside>
    <section class="abs box" style="left:133px;top:213px;width:223px;height:270px">
      <div class="box-head"><svg width="22" height="18" viewBox="0 0 22 18"><circle cx="11" cy="5" r="4" fill="#2a2805"/><circle cx="4" cy="6" r="3" fill="#2a2805"/><circle cx="18" cy="6" r="3" fill="#2a2805"/><path d="M4 17c0-5 3-7 7-7s7 2 7 7z" fill="#2a2805"/></svg>Community</div>
      <ul class="list"><li><i class="tick"></i>Register</li><li><i class="tick"></i>Member Login</li><li><i class="tick"></i>Chat</li><li><i class="tick"></i>Flirtsuche</li><li><i class="tick"></i>Forum</li></ul>
    </section>
    <section class="abs box" style="left:133px;top:501px;width:223px;height:107px">
      <div class="box-head"><svg width="22" height="18" viewBox="0 0 22 18"><path d="M11 0 1 5h20z" fill="#2a2805"/><rect x="3" y="6" width="2.5" height="8" fill="#2a2805"/><rect x="8" y="6" width="2.5" height="8" fill="#2a2805"/><rect x="13" y="6" width="2.5" height="8" fill="#2a2805"/><rect x="18" y="6" width="2.5" height="8" fill="#2a2805"/><rect x="1" y="15" width="21" height="3" fill="#2a2805"/></svg>School &amp; University</div>
      <ul class="list" style="padding-top:12px"><li><i class="tick"></i>Speeches / Housework</li></ul>
    </section>
    <section class="abs box" style="left:133px;top:627px;width:223px;height:107px">
      <div class="box-head"><svg width="17" height="17" viewBox="0 0 17 17"><circle cx="8.5" cy="8.5" r="8.5" fill="#2a2805"/><rect x="7.3" y="7" width="2.4" height="6.5" fill="#fff"/><circle cx="8.5" cy="4.4" r="1.4" fill="#fff"/></svg>Information</div>
      <ul class="list" style="padding-top:12px"><li><i class="tick"></i>FAQs</li></ul>
    </section>
    <section class="abs box" style="left:133px;top:753px;width:223px;height:270px">
      <div class="box-head"><svg width="22" height="16" viewBox="0 0 22 16"><path d="M1 0v15h21" stroke="#2a2805" stroke-width="2" fill="none"/><rect x="5" y="7" width="2.5" height="6" fill="#2a2805"/><rect x="9" y="3" width="2.5" height="10" fill="#2a2805"/><rect x="13" y="5" width="2.5" height="8" fill="#2a2805"/><rect x="17" y="9" width="2.5" height="4" fill="#2a2805"/></svg>Statistics</div>
      <div class="stats"><div><span>Members</span><span>401325</span></div><div><span>Men</span><span>197695</span></div><div><span>women</span><span>196799</span></div><div><span>Presentations</span><span>12458</span></div><div><span>Posts</span><span>3080848</span></div></div>
    </section>
    <section class="abs box" style="left:133px;top:1042px;width:223px;height:177px">
      <div class="box-head"><svg width="22" height="17" viewBox="0 0 22 17"><circle cx="7" cy="5" r="4.5" fill="#2a2805"/><path d="M0 17c0-5 3-7 7-7s7 2 7 7z" fill="#2a2805"/><path d="M18 5v8M14 9h8" stroke="#2a2805" stroke-width="2.4"/></svg>New Member</div>
      <div class="abs" role="img" aria-label="Profile photo of the newest member" style="left:12px;top:62px;width:90px;height:90px;border-radius:50%;background:radial-gradient(circle,#c98b6a 0,#7a4a32 70%);border:3px solid #fff;box-shadow:0 0 4px rgba(0,0,0,.4)"></div>
      <div class="abs" style="left:118px;top:72px;font-size:18px;font-weight:600;color:var(--ink)">Nelira</div>
      <div class="abs" style="left:120px;top:106px;font-size:15px;font-style:italic;line-height:24px">Age: 31 years<br>Profile</div>
    </section>
  </aside>

  <main>
    <div class="abs search">
      <label>KEYWORD:</label>
      <div class="field"><svg class="abs" style="left:18px;top:15px" width="20" height="20" viewBox="0 0 20 20"><circle cx="8" cy="8" r="6" stroke="#bbb" stroke-width="2.5" fill="none"/><path d="M12.5 12.5 18 18" stroke="#bbb" stroke-width="3"/></svg></div>
      <div class="abs btn btn-orange" style="left:515px;top:14px;width:122px;height:48px">Search</div>
    </div>
    <div class="abs hero" role="img" aria-label="Student with glasses working at a laptop in a library"></div>
    <div class="abs hero-text">
      <h1>HELLO VISITOR ,</h1>
      <p>On Lernwinkel.de you will find many papers , specialist work and homework. If you are not able to find a presentation on a topic, you can ask your question in the forum where you are usually helped quickly.<br><b>401325 MEMBERS</b> are already <b>REGISTERED</b><br>with us!</p>
    </div>
    <section class="abs box subjects">
      <div class="box-head"><svg width="22" height="16" viewBox="0 0 22 16"><path d="M1 0v15h21" stroke="#2a2805" stroke-width="2" fill="none"/><path d="M3 14 7 6l4 4 4-7 5 11z" fill="#2a2805"/></svg>Presentations - Homework - Homework for the following subjects:</div>
      <div class="grid">
        <div class="col" style="left:0"><span style="top:0"><i class="tick"></i>English (2937)</span><span style="top:39px"><i class="tick"></i>English (1113)</span><span style="top:78px"><i class="tick"></i>Latin (275)</span><span style="top:117px"><i class="tick"></i>French (196)</span><span style="top:156px"><i class="tick"></i>Italian (32)</span><span style="top:195px"><i class="tick"></i>Greek (28)</span><span style="top:234px"><i class="tick"></i>Spanish (74)</span></div>
        <div class="col" style="left:137px"><span style="top:0"><i class="tick"></i>Mathematics (99)</span><span style="top:39px"><i class="tick"></i>Physics (481)</span><span style="top:78px"><i class="tick"></i>Chemistry (450)</span><span style="top:117px"><i class="tick"></i>Astronomy (82)</span><span style="top:156px"><i class="tick"></i>Geography (785)</span><span style="top:195px"><i class="tick"></i>History (1870)</span><span style="top:234px"><i class="tick"></i>Social Science (555)</span></div>
        <div class="col" style="left:314px"><span style="top:0"><i class="tick"></i>Business (435)</span><span style="top:39px"><i class="tick"></i>Right (109)</span><span style="top:78px"><i class="tick"></i>Music (448)</span><span style="top:117px"><i class="tick"></i>Art (265)</span><span style="top:156px"><i class="tick"></i>Religion (521)</span><span style="top:195px"><i class="tick"></i>Computer(191)</span><span style="top:234px"><i class="tick"></i>Stenography (6)</span></div>
        <div class="col" style="left:467px"><span style="top:0"><i class="tick"></i>Housekeeping (109)</span><span style="top:39px"><i class="tick"></i>Sport (136)</span><span style="top:78px"><i class="tick"></i>Choir (19)</span><span style="top:117px"><i class="tick"></i>Orchestra (5)</span><span style="top:156px"><i class="tick"></i>Biology (1237)</span></div>
      </div>
    </section>
  </main>

  <aside>
    <section class="abs box messenger">
      <div class="box-head"><svg width="20" height="16" viewBox="0 0 20 16"><ellipse cx="8" cy="6" rx="7" ry="5" stroke="#2a2805" stroke-width="2" fill="none"/><path d="M3 10 1 14l5-3M14 6c3 1 5 3 4 6l1 3-4-2" stroke="#2a2805" stroke-width="2" fill="none"/></svg>Live Messenger</div>
      <p class="abs" style="left:10px;top:60px;width:203px;text-align:center;font-size:14.5px;line-height:26px">This feature is only available for members.</p>
      <div class="abs btn btn-orange" style="left:42px;top:124px;width:137px;height:47px">Contact us</div>
      <div class="abs btn btn-ghost" style="left:42px;top:181px;width:137px;height:47px">Login</div>
      <p class="abs" style="left:0;top:242px;width:223px;text-align:center;font-size:14px">No new message</p>
    </section>
    <div class="abs promo" role="img" aria-label="Young woman with a scarf standing by a brick wall"></div>
    <div class="abs" style="left:1044px;top:684px;width:223px;text-align:center;color:#fff;font-weight:700;font-size:25px">AT IT?</div>
    <div class="abs btn btn-orange" style="left:1056px;top:721px;width:200px;height:41px">Register for free</div>
  </aside>

  <footer class="abs footer">
    <p style="margin-top:24px">Home | Department of School - Housework | imprint | data protection | Conditions</p>
    <p style="margin-top:9px">© 2017, Lernwinkel. All rights reserved</p>
  </footer>
</div>
</body>
</html>
```